Design a (20.4 x 10.14) Banner that says - Keep Hope Rising From Harvest Crown TV Family

We want a design (20.4 x 10.14) with the words 'Keep Hope Rising' as the main text and 'From Harvest Crown TV Family' underneath. For 'Harvest Crown TV', we'd like you to use the logo which can be found in the image attached.

The image attached is just an example but please let your creative juices flow!

Target Market(s)

Christian

Industry/Entity Type

Christian

Requirements
Must have
• Must have the words 'Keep Hope Rising' and 'From Harvest Crown TV Family'.

```html
<!DOCTYPE html>
<html lang="en">
<head>
<meta charset="utf-8">
<title>Keep Hope Rising – Harvest Crown TV Family Banner</title>
<link rel="stylesheet" href="https://fonts.googleapis.com/css2?family=Montserrat:wght@600;800&family=Yellowtail&display=swap">
<style>
  :root {
    --page-bg: #f1f1f4;
    --navy-deep: #070b33;
    --leaf-teal: #1f5a70;
    --leaf-navy: #101b4f;
    --violet-left: #4a40b8;
    --violet-right: #5a3a9c;
    --hope-start: #5d5fe3;
    --hope-end: #7a48c2;
    --line-white: #ffffff;
    --tag-grey: #d9d9de;
    --tag-ink: #14163a;
  }
  html, body {
    margin: 0;
    width: 1200px;
    height: 1000px;
    overflow: hidden;
    background: var(--page-bg);
  }
  .canvas {
    position: relative;
    width: 1200px;
    height: 1000px;
  }
  .banner {
    position: absolute;
    left: 0;
    top: 202px;
    width: 1200px;
    height: 596px;
    display: block;
  }
  .title-script {
    font-family: "Yellowtail", cursive;
    fill: var(--line-white);
  }
  .title-hope {
    font-family: "Montserrat", sans-serif;
    font-weight: 800;
  }
  .title-hope-outline {
    fill: none;
    stroke: var(--line-white);
    stroke-width: 3;
  }
  .family-tag-text {
    font-family: "Montserrat", sans-serif;
    font-weight: 600;
    fill: var(--tag-ink);
    letter-spacing: 1px;
  }
</style>
</head>
<body>
<main class="canvas">
  <svg class="banner" viewBox="0 0 1062 527" xmlns="http://www.w3.org/2000/svg" aria-labelledby="banner-title">
    <title id="banner-title">Keep Hope Rising – From Harvest Crown TV Family</title>
    <defs>
      <linearGradient id="leaf-photo-tone" x1="0" y1="0" x2="1" y2="1">
        <stop offset="0" stop-color="var(--leaf-navy)"/>
        <stop offset="0.5" stop-color="var(--leaf-teal)"/>
        <stop offset="1" stop-color="var(--leaf-navy)"/>
      </linearGradient>
      <linearGradient id="violet-left-fill" x1="0" y1="0" x2="1" y2="1">
        <stop offset="0" stop-color="#3c3aa8"/>
        <stop offset="1" stop-color="var(--violet-left)"/>
      </linearGradient>
      <linearGradient id="violet-right-fill" x1="0" y1="0" x2="1" y2="1">
        <stop offset="0" stop-color="var(--violet-left)"/>
        <stop offset="1" stop-color="var(--violet-right)"/>
      </linearGradient>
      <linearGradient id="hope-fill" x1="0" y1="0" x2="1" y2="0">
        <stop offset="0" stop-color="var(--hope-start)"/>
        <stop offset="1" stop-color="var(--hope-end)"/>
      </linearGradient>
    </defs>

    <!-- background photo area -->
    <rect class="leaf-photo" x="0" y="0" width="1062" height="527" fill="url(#leaf-photo-tone)"
          role="img" aria-label="Photograph of dark monstera leaves in deep blue and teal tones"/>

    <!-- side panels -->
    <polygon class="side-panel-left" points="0,0 6,0 336,527 0,527" fill="url(#violet-left-fill)" opacity="0.95"/>
    <polygon class="side-panel-right" points="726,0 1062,0 1062,512" fill="url(#violet-right-fill)" opacity="0.9"/>

    <!-- frame lines -->
    <g class="frame-lines" stroke="var(--line-white)" stroke-width="3" stroke-linecap="round">
      <line x1="14" y1="2" x2="352" y2="527"/>
      <line x1="709" y1="2" x2="1051" y2="527"/>
      <line x1="331" y1="29" x2="220" y2="272"/>
      <line x1="843" y1="261" x2="729" y2="502"/>
    </g>

    <!-- headline -->
    <text class="title-script" x="535" y="168" font-size="104" text-anchor="middle">Keep</text>

    <g class="title-hope">
      <text class="title-hope-outline" x="340" y="338" font-size="150" textLength="405" lengthAdjust="spacingAndGlyphs">HOPE</text>
      <text x="326" y="326" font-size="150" fill="url(#hope-fill)" textLength="405" lengthAdjust="spacingAndGlyphs">HOPE</text>
    </g>

    <text class="title-script" x="530" y="442" font-size="104" text-anchor="middle">Rising</text>

    <!-- family tag -->
    <polygon class="family-tag" points="770,457 1062,457 1062,502 756,502" fill="var(--tag-grey)"/>
    <text class="family-tag-text" x="912" y="485" font-size="13" text-anchor="middle">FROM HARVEST CROWN TV FAMILY</text>
  </svg>
</main>
</body>
</html>
```